Pilates Classes Flyer Design

I need a flyer designed that will promote my range of classes held in Bath, UK. I teach beginners, intermediate level and Over 50's and 60's and also teach individuals in their own homes. I would like to see designs using my colours blue Pantone 306 and Lime Green 14-0452 TPX TCX. The flyer should reflect a friendly, welcoming and professional class structure. I attach an old flyer for your reference and copy.

Target Market(s)

Men and Women who have busy lives working hard, who recognise they need to stretch out, do some exercise and de-stress after a busy day

Ladies over 50 who want to do some Pilates in a friendly fun environment and meet people at the same time.

Industry/Entity Type

It Professional

Font styles to use
Sans Serif
Script

Requirements
Must have
• One-sided flyer
Text only logo. Drop the figure

```html
<!DOCTYPE html>
<html lang="en">
<head>
<meta charset="utf-8">
<title>Stillpoint Pilates – New Classes</title>
<link href="https://fonts.googleapis.com/css2?family=Roboto+Condensed:wght@400;700&family=Lobster+Two:ital,wght@1,400&display=swap" rel="stylesheet">
<style>
  :root {
    --blue: #00a3d4;
    --lime: #c3d98a;
    --lime-deep: #b7d07a;
    --ink: #1d1d1f;
    --text: #2e2e30;
    --paper: #fbfbfa;
    --backdrop: #ecebe7;
  }
  * { margin: 0; padding: 0; box-sizing: border-box; }
  html, body { width: 1200px; height: 963px; overflow: hidden; background: var(--backdrop); }
  .flyer {
    position: absolute; left: 60px; top: 101px;
    width: 1080px; height: 760px;
    background: var(--paper);
    font-family: "Roboto Condensed", "Arial Narrow", sans-serif;
    color: var(--text);
    box-shadow: 0 2px 10px rgba(0,0,0,.12);
  }
  .column { position: absolute; left: 0; width: 880px; text-align: center; }
  .brand {
    top: 50px; font-size: 70px; font-weight: 400;
    color: var(--blue); letter-spacing: 2px; line-height: 1;
  }
  .headline {
    top: 178px; font-family: "Lobster Two", cursive; font-style: italic;
    font-size: 50px; color: var(--blue); line-height: 1;
  }
  .intro { top: 250px; font-size: 21px; font-weight: 700; line-height: 34px; color: #3a3a3c; }
  .features { top: 348px; font-size: 19px; line-height: 34px; color: var(--ink); }
  .features .accent { color: var(--blue); font-weight: 700; }
  .venues-intro { top: 485px; font-size: 19px; color: var(--ink); }
  .venues { top: 523px; font-size: 20px; color: var(--ink); list-style: none; }
  .venues li { height: 43px; line-height: 30px; }
  .venue-name { background: var(--lime); font-weight: 700; padding: 0 3px; }
  .contact-bar {
    position: absolute; left: 0; top: 672px; width: 917px; height: 50px;
    background: var(--blue); color: var(--ink);
    font-size: 27px; font-weight: 700;
    display: flex; align-items: center; padding-left: 38px; gap: 10px;
  }
  .contact-bar svg { width: 22px; height: 22px; flex: none; }
  .contact-bar .gap { margin-right: 8px; }
  .accent-square { position: absolute; left: 1022px; top: 670px; width: 58px; height: 52px; background: var(--lime-deep); }
  .figure-art {
    position: absolute; left: 885px; top: 37px; width: 165px; height: 700px;
    background: linear-gradient(180deg, rgba(0,163,212,.18), rgba(195,217,138,.28) 55%, rgba(0,163,212,.15));
    border-radius: 80px;
  }
</style>
</head>
<body>
  <main class="flyer">
    <div class="column brand">Stillpoint Pilates</div>
    <h1 class="column headline">New Classes Near You!</h1>
    <p class="column intro">Pilates is for EVERYONE whatever level of fitness,<br>age or ability to help you build strength, flexibility and overall well-being.</p>
    <p class="column features">
      <span class="accent">Quality teaching with Core Balance Method Teacher.</span> Progressive approach.<br>
      Teaching good movement skills. <span class="accent">Small class sizes and friendly atmosphere.</span><br>
      Beginners, Intermediate and Over 50’s classes to choose from.
    </p>
    <p class="column venues-intro">Join my one-hour classes at:</p>
    <ul class="column venues">
      <li><span class="venue-name">St Aldric’s Church Hall, Elm Rise</span> Monday evenings, Tuesday and Friday mornings.</li>
      <li><span class="venue-name">Kestrel Meadows Dr. Surgery</span> Tuesday evenings.</li>
      <li><span class="venue-name">Harlow Centre, Mill Road,</span> Wednesday mornings and evenings.</li>
    </ul>
    <div class="figure-art" role="img" aria-label="Line illustration of a stretching figure in blue and lime strokes"></div>
    <div class="contact-bar">
      <span>CALL TESSA ON</span>
      <svg viewBox="0 0 22 22" aria-hidden="true"><circle cx="11" cy="11" r="11" fill="#fff"/><rect x="7.5" y="4.5" width="7" height="13" rx="1.5" fill="none" stroke="#00a3d4" stroke-width="1.5"/><circle cx="11" cy="15" r=".9" fill="#00a3d4"/></svg>
      <span class="gap">07700900123</span>
      <svg viewBox="0 0 22 22" aria-hidden="true"><circle cx="11" cy="11" r="11" fill="#fff"/><rect x="5" y="7" width="12" height="8.5" fill="none" stroke="#00a3d4" stroke-width="1.4"/><path d="M5 7l6 5 6-5" fill="none" stroke="#00a3d4" stroke-width="1.4"/></svg>
      <span>tessa.marlow@example.co.uk</span>
    </div>
    <div class="accent-square"></div>
  </main>
</body>
</html>
```